Flashy Rack Card for Vending Services Company

I am promoting my company that provides vending services for the Sacramento area. Specifically, I provide snack machines and soda machines but with healthy options. If companies prefer the 'standard' options most people are used to (chips, gum, pretzels, etc), I provide that too, but I promote the company as providing healthy alternatives. My options include such options as protein bars, dried fruits and veggies, veggie chips, etc. Instead of soda, I like to provide juices, teas, and protein drinks.

I want a rack card that emphasizes the healthy options and draws on the "you want to be like THIS, not THAT" type of tag line.

Other tag lines I have in my mind draw on the following:

Healthy Vending
Locally owned and operated
Support the community
Grab Kale, Skip Fries

Rack card size:
3.74" x 8.27"
95 x 210 mm
1122 x 2481 pixels

Target Market(s)

Small to medium size businesses, Health Clubs

Industry/Entity Type

It Company

Requirements
Must have
• Images of vending machines, healthy snacks like 'marlo bars' and other similar snacks you would find in a vending machine, company name (Korvaly Vending)
Nice to have
• Images of bottled juices or teas

```html
<!DOCTYPE html>
<html lang="en">
<head>
<meta charset="utf-8">
<title>Korvaly Vending Rack Card</title>
<link href="https://fonts.googleapis.com/css2?family=Oswald:wght@400;500&display=swap" rel="stylesheet">
<style>
  :root {
    --page: #ffffff;
    --green: #7fc241;
    --green-light: #a6d957;
    --yellow: #f6ec2b;
    --ink: #111111;
    --label: #ffffff;
    --frame: #ffffff;
  }
  html, body {
    margin: 0;
    padding: 0;
    width: 1200px;
    height: 2340px;
    overflow: hidden;
    background: var(--page);
  }
  .canvas {
    position: relative;
    width: 1200px;
    height: 2340px;
  }
  .rack-card {
    position: absolute;
    left: 272px;
    top: 512px;
    width: 656px;
    height: 1468px;
    overflow: hidden;
    background: var(--green);
    font-family: 'Oswald', 'Arial Narrow', sans-serif;
  }
  .sunburst-rays {
    position: absolute;
    inset: 0;
  }
  .headline-burst {
    position: absolute;
    left: 128px;
    top: -20px;
    width: 400px;
    height: 330px;
  }
  .headline {
    position: absolute;
    left: 0;
    top: 38px;
    width: 656px;
    margin: 0;
    text-align: center;
    font-weight: 500;
    font-size: 50px;
    line-height: 1.05;
    color: var(--ink);
  }
  .product {
    position: absolute;
    margin: 0;
    border: 10px solid var(--frame);
    box-shadow: 0 4px 10px rgba(0,0,0,0.35);
  }
  .product-photo {
    width: 100%;
    height: 100%;
  }
  .granola { left: 40px;  top: 228px; width: 320px; height: 230px; transform: rotate(-3deg); background: linear-gradient(135deg,#d9b98a,#8a5a35 60%,#c89a63); }
  .water   { left: 372px; top: 250px; width: 200px; height: 220px; transform: rotate(5deg);  background: linear-gradient(160deg,#eaf4fb,#9cc7e6 50%,#2f6fae); }
  .dried   { left: 20px;  top: 490px; width: 320px; height: 280px; transform: rotate(-2deg); background: linear-gradient(135deg,#e8c26a,#b6452c 55%,#f2d9a0); }
  .chips   { left: 320px; top: 480px; width: 300px; height: 250px; transform: rotate(-8deg); background: linear-gradient(135deg,#f29b2e,#e35f1d 50%,#7ab648); }
  .nuts    { left: 130px; top: 770px; width: 370px; height: 220px; border: none; box-shadow: none; background: linear-gradient(135deg,#c79a66,#7a4a2a 50%,#3a2a3a); }
  .machine { left: 522px; top: 790px; width: 92px; height: 140px; border-width: 6px; transform: rotate(4deg); background: linear-gradient(180deg,#3a4a5a,#1e2a36 70%,#5a6a7a); }
  .juices  { left: 24px;  top: 1000px; width: 230px; height: 215px; transform: rotate(-2deg); background: linear-gradient(160deg,#f7f7f7,#c8202e 55%,#f0f0f0); }
  .teas    { left: 290px; top: 985px; width: 260px; height: 215px; transform: rotate(7deg);  background: linear-gradient(160deg,#fbfbfb,#f2b233 45%,#c8282e 75%,#f4f4f4); }
  .label {
    position: absolute;
    margin: 0;
    font-weight: 500;
    font-size: 34px;
    line-height: 1;
    color: var(--label);
    -webkit-text-stroke: 6px var(--ink);
    paint-order: stroke fill;
    white-space: nowrap;
  }
  .label-granola { left: 44px;  top: 232px; transform: rotate(-3deg); }
  .label-water   { left: 640px; top: 300px; transform: rotate(90deg); transform-origin: left top; }
  .label-dried   { left: 28px;  top: 728px; transform: rotate(-6deg); }
  .label-chips   { left: 452px; top: 690px; transform: rotate(-30deg); }
  .label-juices  { left: 40px;  top: 1200px; transform: rotate(-90deg); transform-origin: left top; }
  .label-teas    { left: 570px; top: 955px; transform: rotate(8deg); }
  .footer-band {
    position: absolute;
    left: 0;
    bottom: 0;
    width: 656px;
    height: 236px;
    background: var(--yellow);
    display: flex;
    flex-direction: column;
    justify-content: center;
    align-items: center;
  }
  .footer-band p {
    margin: 0;
    font-weight: 400;
    font-size: 38px;
    line-height: 1.15;
    color: var(--ink);
    text-align: center;
  }
  .footer-band .company-name {
    font-weight: 500;
    font-size: 44px;
  }
  .footer-band .tagline {
    font-weight: 500;
  }
</style>
</head>
<body>
<div class="canvas">
  <section class="rack-card">
    <svg class="sunburst-rays" viewBox="0 0 656 1468" aria-hidden="true">
      <g fill="var(--green-light)" opacity="0.55">
        <polygon points="328,150 0,0 120,0"/>
        <polygon points="328,150 240,0 330,0"/>
        <polygon points="328,150 430,0 540,0"/>
        <polygon points="328,150 656,40 656,180"/>
        <polygon points="328,150 656,420 656,640"/>
        <polygon points="328,150 656,900 656,1150"/>
        <polygon points="328,150 420,1468 200,1468"/>
        <polygon points="328,150 0,1150 0,900"/>
        <polygon points="328,150 0,640 0,420"/>
        <polygon points="328,150 0,180 0,40"/>
      </g>
    </svg>

    <svg class="headline-burst" viewBox="0 0 400 330" aria-hidden="true">
      <polygon fill="var(--yellow)" points="200,0 218,70 262,10 256,84 318,40 290,108 368,90 318,140 398,150 326,180 392,214 314,218 356,270 284,250 296,318 240,270 200,330 168,270 104,318 116,250 44,270 86,218 8,214 74,180 2,150 82,140 32,90 110,108 82,40 144,84 138,10 182,70"/>
    </svg>
    <h1 class="headline">Healthy Vending<br>Available!</h1>

    <figure class="product granola"><div class="product-photo" role="img" aria-label="Photo of granola bars with nuts and dried fruit"></div></figure>
    <figure class="product water"><div class="product-photo" role="img" aria-label="Photo of a bottle of water"></div></figure>
    <figure class="product dried"><div class="product-photo" role="img" aria-label="Photo of mixed dried fruit"></div></figure>
    <figure class="product chips"><div class="product-photo" role="img" aria-label="Photo of colourful veggie chips"></div></figure>
    <figure class="product nuts"><div class="product-photo" role="img" aria-label="Photo of a mixed nuts and raisins trail mix"></div></figure>
    <figure class="product machine"><div class="product-photo" role="img" aria-label="Photo of a snack vending machine stocked with healthy options"></div></figure>
    <figure class="product juices"><div class="product-photo" role="img" aria-label="Photo of a bottled fruit juice drink"></div></figure>
    <figure class="product teas"><div class="product-photo" role="img" aria-label="Photo of a bottled iced tea"></div></figure>

    <p class="label label-granola">Granola Bars</p>
    <p class="label label-water">Bottled Water</p>
    <p class="label label-dried">Dried Fruit</p>
    <p class="label label-chips">Veggie Chips</p>
    <p class="label label-juices">Juices</p>
    <p class="label label-teas">Teas</p>

    <footer class="footer-band">
      <p class="company-name">Korvaly Vending</p>
      <p class="tagline">Grab Kale, Skip Fries</p>
      <p>Locally owned and operated</p>
      <p>Support the community and eat healthy!</p>
    </footer>
  </section>
</div>
</body>
</html>
```